Private law enforcement protective services needs a kick ass brochure

We need a brochure that tops the security competition. We are a Pennsylvania based company providing law enforcement officers to the private sector to take the place of regular security officers. We are peacekeepers with the powers of arrest for any major crime committed in our presence. Our customers will get so much more by using our services over regular security. All of our officers attend annual training to stay up to date and sharp in their skills. We would like to see a design that uses the colors Royal blue, black, and grays. The final design should communicate better service over regular security yet have that soft touch and caring feeling. We want to be taken serious yet not scary. We want prospective customers to say WOW... we need to use them rather than regular security guards. We also offer K-9 services. Drug searches as well as explosive searches. THIS NEEDS TO GO ON A TRI FOLD BROCHURE. I already have a website. Www.northbriarwarden.com

Target Market(s)

Any business or entity where security or protective services will be needed. We provide services for events like Fairs, carnivals, churches, retail stores, large events, hostile terminations, post disaster sites, overarching of work crews in hostile areas, special celebrations, parades, sporting events,

Industry/Entity Type

Security Service

Font styles to use
Sans Serif

Requirements
Must have
• We need to have a strong professional look yet not too aggressive. DO NOT CALL OUR SERVICES SECURITY !!!! We are PEACEKEEPERS. We Keep the Peace. We provide services all across the state of Pennsylvania. We are one of Pennsylvania's best kept secrets.
Nice to have
• Pictures of Police cars, Officers on patrol at an event,

```html
<!DOCTYPE html>
<html lang="en">
<head>
<meta charset="utf-8">
<title>North Briar Warden – Tri-fold Brochure</title>
<link href="https://fonts.googleapis.com/css2?family=Open+Sans:wght@400;600;700;800&display=swap" rel="stylesheet">
<style>
:root{
  --royal:#2e3192;
  --ink:#1f1f1f;
  --paper:#ffffff;
  --stage:#e6e7ea;
  --photo-dark:#15131c;
  --photo-red:#d8352c;
  --photo-violet:#3b2560;
  --photo-stone:#3a3836;
}
*{box-sizing:border-box;margin:0;padding:0}
html,body{width:1154px;height:1200px;overflow:hidden}
body{background:var(--stage);font-family:"Open Sans",Arial,sans-serif;color:var(--ink);position:relative}
.spread{position:absolute;left:177px;width:800px;height:565px;background:var(--paper);box-shadow:0 4px 14px rgba(0,0,0,.18);overflow:hidden}
.spread--outside{top:25px}
.spread--inside{top:610px}
.panel{position:absolute;top:0;height:565px}
.body-copy{font-size:8.6px;line-height:1.33;text-align:justify;hyphens:auto}
/* outside */
.panel--intro{left:0;width:267px}
.panel--intro .body-copy{position:absolute;left:24px;top:26px;width:221px}
.cover-art{position:absolute;left:267px;top:0;width:533px;height:565px}
.intro-art{position:absolute;left:0;top:0;width:267px;height:565px}
.contact{position:absolute;left:267px;top:478px;width:266px;text-align:center;font-size:9px;line-height:1.35}
.contact-icons{display:flex;justify-content:center;gap:4px;margin-bottom:6px}
.contact-icons svg{width:12px;height:12px}
.brand{position:absolute;left:533px;top:460px;width:267px;display:flex;align-items:center;justify-content:center;gap:8px}
.brand-mark{width:26px;height:26px;border-radius:50%;background:var(--royal)}
.brand-name{font-weight:800;font-size:17px;color:var(--royal);letter-spacing:.5px;text-transform:uppercase}
/* inside */
.inside-art{position:absolute;left:0;top:0;width:533px;height:330px}
.who{position:absolute;left:24px;top:338px;width:490px}
.section-title{font-weight:700;font-size:9.6px;text-transform:uppercase;line-height:1.25}
.who .section-title{margin-bottom:7px}
.who-columns{display:flex;gap:46px}
.who-columns .col{width:222px}
.who-columns p{font-size:8.2px;line-height:1.32;text-align:justify;margin-bottom:9px}
.panel--services{left:533px;width:267px;padding:18px 22px 0 23px}
.panel--services .body-copy{font-size:8.2px;margin:8px 0 16px}
.service-grid{display:grid;grid-template-columns:1fr 1fr;row-gap:14px;margin-top:10px}
.service{display:flex;align-items:center;gap:9px;font-size:8.3px;line-height:1.25}
.service-dot{width:30px;height:30px;border-radius:50%;border:2px solid var(--royal);background:#d9dadd;flex:none}
.tagline{text-align:center;margin-top:28px;line-height:1.05}
.tagline .lead{display:block;font-size:17px;font-weight:400}
.tagline .key{display:block;font-size:20px;font-weight:800;color:var(--royal)}
</style>
</head>
<body>

<!-- Outside spread -->
<section class="spread spread--outside">
  <div class="panel panel--intro">
    <svg class="intro-art" viewBox="0 0 267 565" role="img" aria-label="Photograph of an officer's badge in a leather holder resting on handcuffs">
      <defs>
        <linearGradient id="introPhoto" x1="0" y1="0" x2="1" y2="1">
          <stop offset="0" stop-color="#6b6662"/>
          <stop offset=".5" stop-color="var(--photo-stone)"/>
          <stop offset="1" stop-color="#121212"/>
        </linearGradient>
      </defs>
      <path d="M0 298 Q120 250 267 285 L267 565 L0 565 Z" fill="url(#introPhoto)"/>
    </svg>
    <p class="body-copy">The Pennsylvania State Constable is one of the most overlooked entities. Many organizations utilize regular security officers for services to oversee their events, locations, and products simply because they are not aware that constables exist. A Pennsylvania State Constable can perform many of these tasks and address the majority of one's concerns and needs the same as a security officer can. A Pennsylvania State Constable is a Peace Keeper. We keep the peace wherever that may be, for whatever event or incident may be occurring. Unlike security guards, Pennsylvania State Constables are required to attend basic training as well as annual updates to stay refreshed. Security guards do not have any of those requirements. If you have an event, location, or incident that is of concern for the safety and protection of all involved, contact us today to see how we may help you. Not only will you be getting that presence and deterrent, but you will also be getting an actual law enforcement officer. Get more for your money!</p>
  </div>

  <svg class="cover-art" viewBox="0 0 533 565">
    <defs>
      <radialGradient id="coverPhoto" cx=".75" cy=".1" r="1">
        <stop offset="0" stop-color="var(--photo-red)"/>
        <stop offset=".35" stop-color="#8a2a55"/>
        <stop offset=".65" stop-color="var(--photo-violet)"/>
        <stop offset="1" stop-color="var(--photo-dark)"/>
      </radialGradient>
    </defs>
    <path role="img" aria-label="Photograph of a police light bar glowing red and blue at night"
          d="M0 0 H533 V420 Q480 395 430 440 Q395 470 330 440 Q180 370 0 465 Z" fill="url(#coverPhoto)"/>
    <path d="M0 520 Q60 420 240 410 Q120 420 0 480 Z" fill="var(--royal)"/>
  </svg>

  <div class="contact">
    <div class="contact-icons">
      <svg viewBox="0 0 12 12"><circle cx="6" cy="6" r="5.4" fill="none" stroke="var(--royal)" stroke-width="1"/><path d="M4 3.3l1 1.2-.6.7c.4.9 1 1.5 1.9 1.9l.7-.6 1.2 1-.6 1c-2.3-.4-3.9-2-4.3-4.3z" fill="var(--royal)"/></svg>
      <svg viewBox="0 0 12 12"><circle cx="6" cy="6" r="5.4" fill="none" stroke="var(--royal)" stroke-width="1"/><rect x="3.3" y="4.2" width="5.4" height="3.6" fill="var(--royal)"/><path d="M3.3 4.2L6 6.3 8.7 4.2" stroke="#fff" stroke-width=".6" fill="none"/></svg>
      <svg viewBox="0 0 12 12"><circle cx="6" cy="6" r="5.4" fill="none" stroke="var(--royal)" stroke-width="1"/><circle cx="6" cy="6" r="3" fill="none" stroke="var(--royal)" stroke-width=".7"/><path d="M3 6h6M6 3c-1.4 1.7-1.4 4.3 0 6M6 3c1.4 1.7 1.4 4.3 0 6" stroke="var(--royal)" stroke-width=".6" fill="none"/></svg>
    </div>
    <p>+0 123 456 789</p>
    <p>info@yourmail.com</p>
    <p>Www.northbriarwarden.com</p>
  </div>

  <div class="brand">
    <span class="brand-mark"></span>
    <span class="brand-name">North Briar Warden</span>
  </div>
</section>

<!-- Inside spread -->
<section class="spread spread--inside">
  <svg class="inside-art" viewBox="0 0 533 330" role="img" aria-label="Photograph of a service pistol, holster and Pennsylvania State Constable patch on a dark table">
    <defs>
      <linearGradient id="insidePhoto" x1="0" y1="0" x2="1" y2="1">
        <stop offset="0" stop-color="#5c5a57"/>
        <stop offset=".5" stop-color="#2c2b2a"/>
        <stop offset="1" stop-color="#0f0f10"/>
      </linearGradient>
    </defs>
    <path d="M0 0 H533 V282 Q400 360 240 325 Q100 300 0 312 Z" fill="url(#insidePhoto)"/>
  </svg>

  <div class="who">
    <h2 class="section-title">Who we are</h2>
    <div class="who-columns">
      <div class="col">
        <p>Under Pennsylvania Law, Constables are Public Officers elected or appointed to their position in accordance with the laws of elections.</p>
        <p>A Constable is a sworn Law Enforcement/Peace Officer that can arrest for felony crimes and breaches of peace committed in his presence, or by warrant anywhere in the Commonwealth.</p>
        <p>A Constable is also an officer empowered to carry out the business of the statewide district court system by serving warrants of arrest, mental health warrants, transporting prisoners, service of summons, complaints and subpoenas, and enforcing protection from abuse orders, as well as orders of eviction and judgement levies.</p>
      </div>
      <div class="col">
        <p>Constables are also charged with maintaining order at the election polls and ensuring that no qualified elector is obstructed from voting. Constables are the only law enforcement officials permitted at the polls on election day.</p>
        <p>While Constables primarily serve the Courts, they belong to the executive branch of government.</p>
        <p>Constables are empowered to enforce both criminal and civil laws. Police officers are empowered to enforce criminal and traffic laws. The sheriff is empowered to enforce criminal, civil, and traffic laws. The District Attorney is the chief law enforcement officer of the County.</p>
      </div>
    </div>
  </div>

  <div class="panel panel--services">
    <h2 class="section-title">Typical events/locations at which Pennsylvania State Constables provide services:</h2>
    <p class="body-copy">Pennsylvania State Constables are Peace Keepers. A Constable may make a warrant less arrest for any breach of the peace in his or her presence. A breach of the peace by definition in Pennsylvania is any offence that is considered a misdemeanor or felony. Constables work side by side with local and state authorities in many cases around the state. The Pennsylvania State Constable is one of the most overlooked entities around Pennsylvania today. Constables are not security guards, however any where you find event security, you would very easily be able to replace them with a Constable. We are able to function at events and incidents much like a security guard. Our Pennsylvania State Constables will maintain the peace, give you that added presence of law enforcement and peace of mind you deserve.</p>
    <h2 class="section-title">Typical events/locations at which Pennsylvania State Constables provide services:</h2>
    <div class="service-grid">
      <div class="service"><span class="service-dot"></span><span>Public<br>Events</span></div>
      <div class="service"><span class="service-dot"></span><span>Construction /<br>Utility Job Sites</span></div>
      <div class="service"><span class="service-dot"></span><span>Crowd<br>Control</span></div>
      <div class="service"><span class="service-dot"></span><span>Emergencies/<br>Disasters</span></div>
      <div class="service"><span class="service-dot"></span><span>Retail</span></div>
      <div class="service"><span class="service-dot"></span><span>Place of<br>Employment</span></div>
    </div>
    <p class="tagline"><span class="lead">WE ARE</span><span class="key">PEACEKEEPERS</span></p>
  </div>
</section>

</body>
</html>
```